QM Lanterns Business Card

Need a professional but with a touch of unique looking Business Card for my staff.

Target Market(s)

Corporate

Industry/Entity Type

Business

Requirements
Must have
• 40mm height

```html
<!DOCTYPE html>
<html lang="en">
<head>
<meta charset="utf-8">
<title>QM Lanterns Business Card</title>
<link rel="stylesheet" href="https://fonts.googleapis.com/css2?family=Arimo:wght@400;700&display=swap">
<style>
  :root {
    --backdrop: #ebe7e2;
    --card: #ffffff;
    --card-edge: #8a7a6a;
    --brand-grey: #5e5e5e;
    --ink: #1e1e1e;
    --tag-light: #b9b9b9;
    --tag-dark: #5a5a5a;
    --tag-text: #ffffff;
  }
  * { margin: 0; padding: 0; box-sizing: border-box; }
  html, body {
    width: 1200px;
    height: 1071px;
    overflow: hidden;
    background: var(--backdrop);
    font-family: "Arimo", Arial, sans-serif;
  }
  .stage { position: relative; width: 1200px; height: 1071px; }
  .card {
    position: absolute;
    width: 736px;
    height: 419px;
    background: var(--card);
    border: 1px solid var(--card-edge);
  }
  .card--front { left: 81px; top: 80px; }
  .card--back { left: 374px; top: 566px; }

  .brand-name {
    position: absolute;
    color: var(--brand-grey);
    font-weight: 400;
    letter-spacing: -2px;
    line-height: 1;
    white-space: nowrap;
  }
  .card--front .brand-name { left: 46px; top: 58px; font-size: 86px; }
  .card--back .brand-name {
    left: 0; right: 0; top: 185px;
    text-align: center; font-size: 86px;
  }

  .address {
    position: absolute;
    left: 46px; top: 208px;
    font-size: 18px;
    color: var(--ink);
  }
  .contacts {
    position: absolute;
    left: 46px; top: 262px;
    list-style: none;
  }
  .contacts li {
    display: flex;
    align-items: center;
    height: 32.5px;
    font-size: 18px;
    color: var(--ink);
  }
  .contacts svg { width: 16px; height: 16px; margin-right: 9px; fill: var(--ink); }

  .name-tag {
    position: absolute;
    right: -1px; top: 285px;
    width: 252px; height: 85px;
    border-radius: 14px 0 0 14px;
    background: linear-gradient(90deg, var(--tag-light) 0%, #8c8c8c 45%, var(--tag-dark) 100%);
    box-shadow: 0 14px 12px -10px rgba(0,0,0,0.35);
    color: var(--tag-text);
    text-align: center;
    padding-top: 11px;
    padding-right: 20px;
  }
  .name-tag .person { font-size: 28px; font-weight: 700; line-height: 1.1; }
  .name-tag .role { font-size: 23px; line-height: 1.2; }

  .back-url {
    position: absolute;
    left: 0; right: 0; top: 346px;
    text-align: center;
    font-size: 20px;
    letter-spacing: 4px;
    color: var(--brand-grey);
  }
</style>
</head>
<body>
<main class="stage">
  <section class="card card--front">
    <div class="brand-name">QM Lanterns</div>
    <p class="address">Street Name, City, State, zip code</p>
    <ul class="contacts">
      <li>
        <svg viewBox="0 0 16 16" aria-hidden="true"><path d="M8 1a7 7 0 1 0 0 14A7 7 0 0 0 8 1zm0 1.4a5.6 5.6 0 1 1 0 11.2A5.6 5.6 0 0 1 8 2.4zM6 4.5l1.2 1.8-.8.9c.5 1 1.3 1.9 2.3 2.4l.9-.8 1.8 1.2-.6 1.3c-2.7-.3-5.2-2.8-5.4-5.5z"/></svg>
        123-456-7890
      </li>
      <li>
        <svg viewBox="0 0 16 16" aria-hidden="true"><path d="M4 1h6l2 2v3H4zM2 7h12a1 1 0 0 1 1 1v5H1V8a1 1 0 0 1 1-1zm2 3v5h8v-5z"/></svg>
        123-456-7890
      </li>
      <li>
        <svg viewBox="0 0 16 16" aria-hidden="true"><path d="M1 4h14v9H1zm1 .8v.6L8 9l6-3.6v-.6z"/></svg>
        hello@qmlanterns.com
      </li>
      <li>
        <svg viewBox="0 0 16 16" aria-hidden="true"><path d="M8 1.5a6.5 6.5 0 1 0 0 13 6.5 6.5 0 0 0 0-13zm-1 1.2v2.8H4.2A5.3 5.3 0 0 1 7 2.7zm2 0a5.3 5.3 0 0 1 2.8 2.8H9zM3.6 7H7v2H3.6a5.4 5.4 0 0 1 0-2zM9 7h3.4a5.4 5.4 0 0 1 0 2H9zm-4.8 3.5H7v2.8a5.3 5.3 0 0 1-2.8-2.8zm4.8 0h2.8A5.3 5.3 0 0 1 9 13.3z"/></svg>
        www.qmlanterns.com
      </li>
    </ul>
    <div class="name-tag">
      <div class="person">Your Name</div>
      <div class="role">Title</div>
    </div>
  </section>

  <section class="card card--back">
    <div class="brand-name">QM Lanterns</div>
    <p class="back-url">www.qmlanterns.com</p>
  </section>
</main>
</body>
</html>
```